Startup photography business has a new logo, now we need business cards

Design a business card for the two partners of our business.
Our business Brisk Pelican has a new logo and we need to design a business card to showcase it and us.
Our colours of blue and orange are punchy and vivid, but how can we make the most of it on our card?

It should have our name Brisk Pelican
name of partner
phone number
email
website

Industry/Entity Type

Professional Photography

Contact Information for Business Card

Tom Ashworth
+61 400 55 61 72
tom@briskpelican.com.au
briskpelican.com.au

second card
Neil Porter
+61 400 918 263
neil@briskpelican.com.au
briskpelican.com.au

Colors
f37122
f68d4c
33a6d7
0592cd

Requirements
Must have
• one version of our logo, we have included options
• Name
• phone number
• email
• website
Nice to have
• instagram briskpelicanmedia
• twitter briskpelicanmedia
• facebook briskpelicanmedia

```html
<!DOCTYPE html>
<html lang="en">
<head>
<meta charset="utf-8">
<title>Brisk Pelican – Business Card</title>
<link rel="stylesheet" href="https://fonts.googleapis.com/css2?family=Arimo:wght@400;700&display=swap">
<style>
  :root {
    --stage: #2a2a2a;
    --sky: #29bdef;
    --sky-deep: #1aa9de;
    --orange: #f37122;
    --paper: #ececec;
    --white: #ffffff;
  }
  * { box-sizing: border-box; margin: 0; padding: 0; }
  html, body { width: 1200px; height: 900px; overflow: hidden; }
  body {
    background: var(--stage);
    font-family: "Arimo", Arial, sans-serif;
    display: flex;
    flex-direction: column;
    align-items: center;
    justify-content: center;
    gap: 40px;
  }
  .card {
    position: relative;
    width: 700px;
    height: 390px;
    border-radius: 22px;
    overflow: hidden;
  }

  /* Back side */
  .card-back { background: var(--sky); }
  .card-back .edge-strip {
    position: absolute;
    background: var(--white);
    width: 190px;
    height: 14px;
  }
  .card-back .edge-strip.top { top: 22px; right: 0; }
  .card-back .edge-strip.bottom { bottom: 22px; left: 0; }
  .back-mark {
    position: absolute;
    inset: 0;
    display: flex;
    align-items: center;
    justify-content: center;
    gap: 16px;
  }
  .back-mark .dot {
    width: 44px; height: 44px;
    border: 6px solid var(--orange);
    border-radius: 50%;
  }
  .back-mark .brand-name {
    color: var(--white);
    font-weight: 700;
    font-size: 46px;
    letter-spacing: 1px;
  }

  /* Front side */
  .card-front { background: var(--paper); }
  .front-brand {
    position: absolute;
    left: 50px;
    top: 110px;
    width: 300px;
    display: flex;
    align-items: center;
    gap: 12px;
  }
  .front-brand .dot {
    width: 34px; height: 34px;
    border-radius: 50%;
    background: var(--orange);
    flex: none;
  }
  .front-brand .brand-name {
    color: var(--sky);
    font-weight: 700;
    font-size: 36px;
    white-space: nowrap;
  }
  .divider {
    position: absolute;
    left: 385px;
    top: 50px;
    width: 2px;
    height: 180px;
    background: linear-gradient(to bottom, transparent, var(--sky-deep), transparent);
  }
  .contact {
    position: absolute;
    left: 420px;
    top: 58px;
  }
  .contact .person {
    color: var(--sky);
    font-weight: 700;
    font-size: 22px;
  }
  .contact .role {
    color: var(--orange);
    font-size: 16px;
    margin: 4px 0 12px 14px;
  }
  .contact ul { list-style: none; margin-left: 26px; }
  .contact li {
    display: flex;
    align-items: center;
    gap: 10px;
    color: var(--sky);
    font-size: 16px;
    margin-bottom: 10px;
  }
  .contact li svg { width: 18px; height: 18px; flex: none; }

  .community-band {
    position: absolute;
    left: 0; right: 0; bottom: 0;
    height: 120px;
    background: var(--sky);
    color: var(--white);
    text-align: center;
    padding-top: 20px;
  }
  .community-band .invite { font-size: 16px; margin-bottom: 16px; }
  .handles {
    list-style: none;
    display: flex;
    justify-content: center;
    gap: 42px;
  }
  .handles li {
    display: flex;
    flex-direction: column;
    align-items: center;
    gap: 6px;
    font-size: 15px;
  }
  .handles .dot {
    width: 16px; height: 16px;
    border-radius: 50%;
    background: var(--white);
  }
</style>
</head>
<body>

<section class="card card-back">
  <span class="edge-strip top"></span>
  <span class="edge-strip bottom"></span>
  <div class="back-mark">
    <span class="dot"></span>
    <span class="brand-name">Brisk Pelican</span>
  </div>
</section>

<section class="card card-front">
  <div class="front-brand">
    <span class="dot"></span>
    <span class="brand-name">Brisk Pelican</span>
  </div>

  <span class="divider"></span>

  <div class="contact">
    <p class="person">Neil Porter</p>
    <p class="role">Title</p>
    <ul>
      <li>
        <svg viewBox="0 0 20 20" fill="none" stroke="#f37122" stroke-width="1.8">
          <circle cx="10" cy="10" r="8.5"/>
          <path d="M7 5.5l1.6 2.4-1 1.2c.7 1.5 1.8 2.6 3.3 3.3l1.2-1 2.4 1.6-1 1.5c-3.6-.4-6.6-3.4-7-7z" fill="#f37122" stroke="none"/>
        </svg>
        +61 400 918 263
      </li>
      <li>
        <svg viewBox="0 0 20 20" fill="none" stroke="#f37122" stroke-width="1.8">
          <rect x="2" y="4.5" width="16" height="11"/>
          <path d="M2 4.5l8 6.5 8-6.5M2 15.5l6-5M18 15.5l-6-5"/>
        </svg>
        neil@briskpelican.com.au
      </li>
      <li>
        <svg viewBox="0 0 20 20" fill="none" stroke="#f37122" stroke-width="1.6">
          <circle cx="10" cy="10" r="8.5" fill="#f37122"/>
          <path d="M1.5 10h17M10 1.5v17M4 5.5h12M4 14.5h12" stroke="#ececec" stroke-width="1.2"/>
        </svg>
        www.briskpelican.com.au
      </li>
    </ul>
  </div>

  <footer class="community-band">
    <p class="invite">Join our community</p>
    <ul class="handles">
      <li><span class="dot"></span>@briskpelicanmedia</li>
      <li><span class="dot"></span>briskpelicanmedia</li>
      <li><span class="dot"></span>briskpelicanmedia</li>
    </ul>
  </footer>
</section>

</body>
</html>
```